WebDesign | Financial Services Firm - Risk Mitigation

We are a professional services consulting firm that specializes in high net worth individuals over $25,000,000, executives C-suite and above, closely held businesses owners, family offices and highly compensated employees.

Our focus is on risk mitigation and tax efficient strategies. Our clients take their risk on themselves and have a proven track record generating wealth. Our directive is to preserve and protect the wealth they’ve already created.

Our company Harbinger Collective is geared around five directives of asset protection:
1) Legal Structuring
2) Leverage & Financing
3) Risk Management - Asset Protection & Insurance, Trustee Work
4) Asset Management & Investing - Under www.dvkfarcoast.com
5) Tax Efficient Strategies

Our Company Mark is a Pentagon with a key in the middle. A pentagon is the most efficient defensive structure. Each point of a pentagon is equal distance front every point . Each side provides support to another and works together, which is the key to our clients success.

Our key colors are blue, black and silver.

We ‘re located in the Pacific Northwest with bi coastal and international clients. We have fewer, higher net worth clients and provide exceptional customer service. We do not do social media.

We'll need the following pages:
-Front Landing Page.
Front page has to have link to hcportal.filevaultly.net for logging into secure site.
- Contact & About Us Page
- Our Team Page
- Five Sides of Wealth Management
> Legal & Business Structuring
> Leverage & Financing
> Risk Management & Asset Protection.
> Asset Management and Investing - Will link to DVK (won't be turned on for a few months)
> Tax Efficient Strategies.

Industry/Entity Type

Financial Service

Coding

Coded - Design and coding required

Number of Pages Required

5+ page

Font styles to use
Sans Serif

Colors
0555a3

Requirements
Must have
• Our key colors are blue, black and silver.

-Front Landing Page.
- Contact & About Us Page
- Our Team Page
> Leverage & Financing
Nice to have
• I have attached images that have been purchased for use on the webpage. Us or not.

location page: 872 W Birchwood Ave, Suite 114, Cedar Bluff, OR 97981
Should not have
• lots of color.

```html
<!DOCTYPE html>
<html lang="en">
<head>
<meta charset="utf-8">
<title>Contact Us — Harbinger Collective</title>
<link rel="stylesheet" href="https://fonts.googleapis.com/css2?family=Cinzel:wght@500;600;700&family=Poppins:wght@500;600;700&family=Questrial&display=swap">
<style>
:root{
  --navy:#0d2a6e;
  --blue:#0a9ad6;
  --blue-deep:#0555a3;
  --ink:#1d1d1d;
  --white:#ffffff;
  --line:#e3e6ea;
  --muted:#9aa0a6;
  --footer:#121212;
  --footer-text:#a9a9a9;
  --map:#cfe3ef;
  --hero-a:#3a3f44;
  --hero-b:#23282d;
}
*{box-sizing:border-box;margin:0;padding:0}
html,body{width:1177px;height:1200px;overflow:hidden;background:var(--white)}
body{position:relative;font-family:"Questrial",sans-serif;color:var(--ink)}
.abs{position:absolute}

.hero{left:0;top:0;width:1177px;height:399px;background:linear-gradient(160deg,var(--hero-a),var(--hero-b) 70%,#2f363c)}
.site-header{left:0;top:0;width:1177px;height:66px;border-bottom:1px solid rgba(255,255,255,.22)}
.brand{left:38px;top:22px;display:flex;align-items:center;gap:8px;color:var(--white);font-family:"Cinzel",serif;font-weight:600;font-size:13px;letter-spacing:.6px;white-space:nowrap}
.brand-square{width:12px;height:12px;background:var(--white)}
.main-nav{top:25px;font-family:"Poppins",sans-serif;font-weight:500;font-size:10px;letter-spacing:2.4px;color:var(--white)}
.main-nav span{position:absolute;white-space:nowrap}
.cta-secure{left:989px;top:15px;width:150px;height:34px;border:1px solid var(--blue);border-radius:17px;color:var(--white);font-family:"Poppins",sans-serif;font-weight:600;font-size:8px;letter-spacing:.6px;display:flex;align-items:center;justify-content:center}
.page-title{left:198px;top:287px;font-family:"Cinzel",serif;font-weight:600;font-size:35px;color:var(--white);letter-spacing:.5px;white-space:nowrap}

.form-card{left:518px;top:158px;width:480px;height:520px;background:var(--white);box-shadow:0 10px 30px rgba(0,0,0,.12)}
.card-brand{left:0;top:54px;width:480px;text-align:center;font-family:"Cinzel",serif;font-weight:600;font-size:17px;color:var(--navy);letter-spacing:1px}
.card-title{left:0;top:132px;width:480px;text-align:center;font-family:"Cinzel",serif;font-weight:600;font-size:27px;line-height:34px;color:var(--navy)}
.field{border:1px solid var(--line);font-size:9px;color:var(--muted);padding:10px 7px;font-family:"Poppins",sans-serif}
.btn-contact{left:166px;top:446px;width:150px;height:34px;border-radius:17px;background:var(--blue);color:var(--white);font-family:"Poppins",sans-serif;font-weight:700;font-size:8.5px;letter-spacing:1px;display:flex;align-items:center;justify-content:center}

.contact-item{left:213px;display:flex;gap:10px;align-items:flex-start;font-size:11.5px;line-height:21px;white-space:nowrap}
.contact-item svg{flex:none;margin-top:4px}
.contact-phone{color:var(--blue);font-family:"Poppins",sans-serif;font-weight:600;font-size:13px}
.rule{left:215px;width:164px;height:1px;background:var(--line)}

.map{left:0;top:640px;width:1177px;height:289px;background:linear-gradient(100deg,var(--map),#dbeaf3 50%,#c8deeb)}
.location-card{left:197px;top:685px;width:191px;height:209px;background:var(--white);text-align:center}
.location-card .loc-brand{position:absolute;left:0;top:44px;width:191px;font-family:"Cinzel",serif;font-weight:600;font-size:12px;color:var(--navy);letter-spacing:.5px}
.location-card .loc-line{position:absolute;left:0;top:108px;width:191px;height:1px;background:var(--line)}
.location-card .loc-pin{position:absolute;left:84px;top:96px;background:var(--white);padding:0 3px}
.location-card .loc-label{position:absolute;left:0;top:140px;width:191px;font-family:"Poppins",sans-serif;font-weight:700;font-size:9px;color:var(--navy);letter-spacing:.4px}
.location-card .loc-address{position:absolute;left:10px;top:160px;width:171px;font-size:10px;line-height:14px;color:var(--blue)}

.site-footer{left:0;top:929px;width:1177px;height:271px;background:var(--footer);color:var(--footer-text)}
.f-head{top:49px;font-family:"Cinzel",serif;font-weight:500;font-size:13.5px;letter-spacing:1.4px;color:var(--white);white-space:nowrap}
.f-text{top:86px;font-size:10px;line-height:17.5px}
.f-links{top:86px;font-size:10px;line-height:23px;list-style:none}
.subscribe{left:774px;top:133px;width:202px;height:29px;background:var(--white);font-size:8.5px;color:#777;padding:9px 9px}
.subscribe-btn{left:946px;top:133px;width:30px;height:30px;border-radius:50%;background:linear-gradient(135deg,var(--blue),var(--blue-deep));display:flex;align-items:center;justify-content:center}
.f-divider{left:0;top:224px;width:1177px;height:1px;background:#2b2b2b}
.f-copy{left:192px;top:243px;font-family:Arial,sans-serif;font-size:8.5px;color:#9a9a9a}
.f-copy b{color:var(--white);font-weight:400;margin-left:3px}
.f-legal{left:834px;top:243px;font-family:Arial,sans-serif;font-size:8.5px;color:#9a9a9a}
</style>
</head>
<body>

<div class="hero abs" role="img" aria-label="Photograph of a stone-faced storefront street, darkened as hero background"></div>

<header class="site-header abs">
  <div class="brand abs"><span class="brand-square"></span>Harbinger Collective</div>
  <nav class="main-nav abs" style="left:0">
    <span style="left:360px">HOME</span>
    <span style="left:449px">ABOUT</span>
    <span style="left:545px">STRATEGIES</span>
    <span style="left:672px">TEAM</span>
    <span style="left:757px">CONTACT</span>
  </nav>
  <div class="cta-secure abs">SECURE MY ASSETS</div>
</header>

<h1 class="page-title abs">CONTACT US</h1>

<div class="map abs" role="img" aria-label="Street map of the surrounding area with the office location marked"></div>

<div class="location-card abs">
  <div class="loc-brand">Harbinger Collective</div>
  <div class="loc-line"></div>
  <div class="loc-pin">
    <svg width="18" height="24" viewBox="0 0 18 24" fill="none" stroke="#0a9ad6" stroke-width="1.4"><path d="M9 23s-8-8.5-8-14a8 8 0 0 1 16 0c0 5.5-8 14-8 14z"/><circle cx="9" cy="9" r="3"/></svg>
  </div>
  <div class="loc-label">OUR LOCATION</div>
  <div class="loc-address">872 W Birchwood Ave, Suite 114, Cedar Bluff, OR 97981</div>
</div>

<div class="contact-item abs" style="top:438px">
  <svg width="16" height="13" viewBox="0 0 16 13" fill="none" stroke="#0a9ad6" stroke-width="1.3"><path d="M1 2.5l4.5-1.5 5 1.5 4.5-1.5v9.5l-4.5 1.5-5-1.5L1 12z"/><path d="M5.5 1v9.5M10.5 2.5V12"/></svg>
  <div>872 W Birchwood Ave, Suite 114,<br>Cedar Bluff, OR 97981</div>
</div>
<div class="rule abs" style="top:496px"></div>
<div class="contact-item abs" style="top:512px">
  <svg width="14" height="14" viewBox="0 0 14 14" fill="none" stroke="#0a9ad6" stroke-width="1.3"><path d="M3 1l2 3-1.3 1.3a8 8 0 0 0 5 5L10 9l3 2-1 2c-6 .5-11.5-5-11-11z"/></svg>
  <div class="contact-phone">123-456-7890</div>
</div>
<div class="rule abs" style="top:553px"></div>
<div class="contact-item abs" style="top:568px">
  <svg width="14" height="11" viewBox="0 0 14 11" fill="none" stroke="#0a9ad6" stroke-width="1.3"><rect x="1" y="1" width="12" height="9"/><path d="M1 1l6 5 6-5"/></svg>
  <div>office@harbingermail.net</div>
</div>

<section class="form-card abs">
  <div class="card-brand abs">Harbinger Collective</div>
  <h2 class="card-title abs">GET WEALTH<br>PROTECTION NOW!</h2>
  <div class="field abs" style="left:42px;top:218px;width:194px;height:37px">Name</div>
  <div class="field abs" style="left:244px;top:218px;width:194px;height:37px">Phone</div>
  <div class="field abs" style="left:42px;top:264px;width:396px;height:37px">Email</div>
  <div class="field abs" style="left:42px;top:310px;width:396px;height:92px">Message</div>
  <div class="btn-contact abs">CONTACT US</div>
</section>

<footer class="site-footer abs">
  <h3 class="f-head abs" style="left:192px">ABOUT US</h3>
  <p class="f-text abs" style="left:192px;width:165px">Lorem ipsum dolor sit dolor sit an amet, consectetur adipiscing elit, dolor sed do eiusmod tempor incididunt ut labore.</p>

  <h3 class="f-head abs" style="left:410px">QUICK LINK</h3>
  <ul class="f-links abs" style="left:410px">
    <li>Home</li><li>About</li><li>Strategies</li><li>Team</li><li>Contact</li>
  </ul>

  <h3 class="f-head abs" style="left:563px">STRATEGIES</h3>
  <ul class="f-links abs" style="left:563px">
    <li>Legal Structuring</li><li>Leverage &amp; Financing</li><li>Risk Management</li><li>Asset Management &amp; Investing</li><li>Tax Efficient Strategies</li>
  </ul>

  <h3 class="f-head abs" style="left:773px">SUBSCRIBE TO NEWSLETTERS</h3>
  <p class="f-text abs" style="left:773px;width:200px;line-height:14px;top:86px">Lorem ipsum dolor sit amet, coctetur dipiscing elit, sed do eiuod tempor.</p>
  <div class="subscribe abs">Your Email</div>
  <div class="subscribe-btn abs">
    <svg width="14" height="8" viewBox="0 0 14 8" fill="none" stroke="#fff" stroke-width="1.4"><path d="M0 4h13M9.5 1L13 4 9.5 7"/></svg>
  </div>

  <div class="f-divider abs"></div>
  <div class="f-copy abs">© 2021 <b>HARBINGER COLLECTIVE</b></div>
  <div class="f-legal abs">Privacy Policy &nbsp;|&nbsp; Terms and Conditions</div>
</footer>

</body>
</html>
```